Sales Presentation Powerpoint

This project is to design a sales presentation for a new service/product for hotels.
The product is called snug stay and is a tablet pc that we propose to install in hotel rooms free of charge to hotels. The system has information about the hotel, room service menus, entertainment such as games, web browser, and other functions.
Marketing material has already been designed and the sell sheet that was recently completed is attached for your use.

Additionally, you will need to visit www.snugstaypad.example to see a demo of the product.

PRESENTATION REQUIRMENTS
General requirements – We will select the presentation that is the most visually crisp and stunning, stays within our already established visual themes, and includes multimedia. Interactivity and movement is a big plus if you can incorporate it into the presentation. We will be recording voiceover work on the presentation after it is made so you can plan around that thought.

PRESENTATION FLOW
1. General introduction to the product and what it is (info found on the sell sheet or you can contact me for more details if needed.
2. advantages of the product. Info found on the sell sheet or you can contact me for more details. Each of the main points on the sell sheet need to be a separate slide though so we can speak to it.
3. walkthrough of the product. I would like an animation, screen shots, or something similar to give the view the chance to experience and see the software. The demo at www.snugstaypad.example is the best place to go for that.

Recommendation for design:
Can we have the presentation be framed in a tablet window. to clarify, the border around the presentation is a tablet pc and the presentation appears inside of that.

Tools:
please feel free to use any software. does not need to be powerpoint. if you feel comfortable with solutions such as slidora, deckwave, or any other system you may use that.
Updates

Target Market(s)

presentation is for potential customers

Industry/Entity Type

Entertainment

Requirements
Must have
• visually crisp, sharp, and stunning
adheres to already established style from sell sheet and website.
multimedia encorporation a big plus.

```html
<!DOCTYPE html>
<html lang="en">
<head>
<meta charset="utf-8">
<title>Snug Stay – Sales Presentation</title>
<link href="https://fonts.googleapis.com/css2?family=Dosis:wght@400;600;700&display=swap" rel="stylesheet">
<style>
  :root {
    --canvas: #b3b3b3;
    --paper: #ffffff;
    --brand-red: #d7141c;
    --deep-red: #8e0b10;
    --ink: #1b1b1b;
    --body-text: #2a2a2a;
  }
  html, body { margin: 0; padding: 0; overflow: hidden; }
  body {
    width: 875px; height: 1200px; position: relative;
    background: var(--canvas);
    font-family: "Dosis", sans-serif;
    color: var(--body-text);
  }
  .slide {
    position: absolute; width: 306px; height: 182px;
    background: var(--paper); overflow: hidden;
  }
  .slide .swoosh { position: absolute; left: 0; top: 0; width: 306px; height: 182px; }
  .brand {
    position: absolute; display: flex; align-items: center; gap: 3px;
    color: var(--ink); font-weight: 700;
  }
  .brand .dot { border-radius: 50%; background: var(--brand-red); }
  .brand-tag { position: absolute; font-size: 2.6px; letter-spacing: 0.6px; color: var(--brand-red); }
  .brand--small { left: 12px; top: 12px; font-size: 5.5px; }
  .brand--small .dot { width: 13px; height: 13px; }
  .brand--large { left: 208px; top: 20px; font-size: 8px; }
  .brand--large .dot { width: 22px; height: 22px; }
  .slide-title {
    position: absolute; left: 110px; margin: 0;
    color: var(--brand-red); font-weight: 400; font-size: 10px;
  }
  .slide-body {
    position: absolute; left: 110px; width: 172px; margin: 0;
    font-size: 4.3px; line-height: 5.3px; text-align: justify;
  }
  .slide-body strong { color: var(--ink); font-size: 5.5px; font-weight: 700; }
  .slide-body p { margin: 0 0 5px; }
  .url { position: absolute; font-size: 4px; }
  .url--footer { left: 12px; bottom: 7px; color: var(--paper); }
  .cover-title {
    position: absolute; left: 14px; top: 139px; margin: 0;
    color: var(--brand-red); font-size: 17px; font-weight: 700; line-height: 1;
  }
  .cover-sub { position: absolute; left: 14px; top: 157px; margin: 0; font-size: 6px; color: var(--ink); }
  .url--cover { right: 16px; top: 161px; color: var(--ink); }
  .contact { position: absolute; right: 16px; top: 150px; font-size: 4.5px; color: var(--ink); text-align: left; }
  .contact b { font-size: 7px; }
  .contact .mail { display: flex; align-items: center; gap: 2px; font-size: 3.5px; margin-top: 1px; }
  .contact .mail i { width: 4px; height: 3px; background: var(--brand-red); display: inline-block; }
</style>
</head>
<body>

<svg width="0" height="0" style="position:absolute" aria-hidden="true">
  <defs>
    <linearGradient id="redBand" x1="0" x2="1" y1="0" y2="0">
      <stop offset="0" stop-color="var(--deep-red)"/>
      <stop offset="0.55" stop-color="var(--brand-red)"/>
      <stop offset="1" stop-color="var(--deep-red)"/>
    </linearGradient>
    <symbol id="coverSwoosh" viewBox="0 0 306 182">
      <path d="M0 6 C70 70 190 100 306 96 L306 103 C190 110 70 84 0 26Z" fill="#1b1b1b"/>
      <path d="M0 30 C70 88 190 114 306 106 L306 124 C200 132 80 124 0 78Z" fill="url(#redBand)"/>
    </symbol>
    <symbol id="footerSwoosh" viewBox="0 0 306 182">
      <path d="M0 112 Q150 188 306 116 L306 182 L0 182Z" fill="#1b1b1b"/>
      <path d="M0 132 Q150 196 306 128 L306 182 L0 182Z" fill="#ffffff"/>
      <path d="M0 135 Q150 199 306 131 L306 182 L0 182Z" fill="url(#redBand)"/>
    </symbol>
  </defs>
</svg>

<!-- Cover -->
<section class="slide slide--cover" style="left:78px; top:77px;">
  <svg class="swoosh"><use href="#coverSwoosh"/></svg>
  <div class="brand brand--large"><span class="dot"></span>Snug Stay</div>
  <span class="brand-tag" style="left:208px; top:46px;">HOTEL TECHNOLOGY SOLUTIONS</span>
  <h1 class="cover-title">Snug Stay</h1>
  <p class="cover-sub">No Cost Smart Tablet Technology Program</p>
  <span class="url url--cover">www.snugstaypad.example</span>
</section>

<!-- Complete Solution -->
<section class="slide" style="left:491px; top:77px;">
  <svg class="swoosh"><use href="#footerSwoosh"/></svg>
  <div class="brand brand--small"><span class="dot"></span>Snug Stay</div>
  <span class="brand-tag" style="left:12px; top:28px;">HOTEL TECHNOLOGY SOLUTIONS</span>
  <h2 class="slide-title" style="top:44px;">Complete Solution</h2>
  <p class="slide-body" style="top:64px;">Lorem Ipsum is simply dummy text of the printing and typesetting industry. Lorem Ipsum has been the industry's standard dummy text ever since the 1500s, when an unknown printer took a galley of type and scrambled it to make a type specimen book. It has survived not only five centuries, but also the leap into electronic typesetting, remaining essentially unchanged. It was popularised in the 1960s with the release of Lettrafix sheets containing Lorem Ipsum passages, and more recently with desktop publishing software like Quire Layout including versions of Lorem Ipsum.</p>
  <span class="url url--footer">www.snugstaypad.example</span>
</section>

<!-- How it works -->
<section class="slide" style="left:78px; top:370px;">
  <svg class="swoosh"><use href="#footerSwoosh"/></svg>
  <div class="brand brand--small"><span class="dot"></span>Snug Stay</div>
  <span class="brand-tag" style="left:12px; top:28px;">HOTEL TECHNOLOGY SOLUTIONS</span>
  <h2 class="slide-title" style="top:38px;">How it works</h2>
  <p class="slide-body" style="top:58px;">Lorem Ipsum is simply dummy text of the printing and typesetting industry. Lorem Ipsum has been the industry's standard dummy text ever since the 1500s, when an unknown printer took a galley of type and scrambled it to make a type specimen book. It has survived not only five centuries, but also the leap into electronic typesetting, remaining essentially unchanged. It was popularised in the 1960s with the release of Lettrafix sheets containing Lorem Ipsum passages, and more recently with desktop publishing software like Quire Layout including versions of Lorem Ipsum.</p>
  <span class="url url--footer">www.snugstaypad.example</span>
</section>

<!-- Customer Experience -->
<section class="slide" style="left:491px; top:370px;">
  <svg class="swoosh"><use href="#footerSwoosh"/></svg>
  <div class="brand brand--small"><span class="dot"></span>Snug Stay</div>
  <span class="brand-tag" style="left:12px; top:28px;">HOTEL TECHNOLOGY SOLUTIONS</span>
  <h2 class="slide-title" style="top:38px;">Customer Experience</h2>
  <p class="slide-body" style="top:58px;">Lorem Ipsum is simply dummy text of the printing and typesetting industry. Lorem Ipsum has been the industry's standard dummy text ever since the 1500s, when an unknown printer took a galley of type and scrambled it to make a type specimen book. It has survived not only five centuries, but also the leap into electronic typesetting, remaining essentially unchanged. It was popularised in the 1960s with the release of Lettrafix sheets containing Lorem Ipsum passages, and more recently with desktop publishing software like Quire Layout including versions of Lorem Ipsum.</p>
  <span class="url url--footer">www.snugstaypad.example</span>
</section>

<!-- Key Benefits 1 -->
<section class="slide" style="left:78px; top:660px;">
  <svg class="swoosh"><use href="#footerSwoosh"/></svg>
  <div class="brand brand--small"><span class="dot"></span>Snug Stay</div>
  <span class="brand-tag" style="left:12px; top:28px;">HOTEL TECHNOLOGY SOLUTIONS</span>
  <h2 class="slide-title" style="top:38px;">Key Benefits</h2>
  <div class="slide-body" style="top:57px;">
    <p><strong>Data Base</strong> Lorem Ipsum is simply dummy text of the printing and typesetting industry. Lorem Ipsum has been the industry's standard dummy text ever since the 1500s, when an unknown printer took a galley of type and scrambled it to make a type specimen book. It has survived not only five centuries, but also the leap into electronic typesetting, remaining essentially unchanged.</p>
    <p><strong>Competitive Technology</strong> Lorem Ipsum is simply dummy text of the printing and typesetting industry. Lorem Ipsum has been the industry's standard dummy text ever since the 1500s, when an unknown printer took a galley of type and scrambled it to make a type specimen book. It has survived not only five centuries, but also the leap into electronic typesetting, remaining essentially unchanged.</p>
  </div>
  <span class="url url--footer">www.snugstaypad.example</span>
</section>

<!-- Key Benefits 2 -->
<section class="slide" style="left:491px; top:660px;">
  <svg class="swoosh"><use href="#footerSwoosh"/></svg>
  <div class="brand brand--small"><span class="dot"></span>Snug Stay</div>
  <span class="brand-tag" style="left:12px; top:28px;">HOTEL TECHNOLOGY SOLUTIONS</span>
  <h2 class="slide-title" style="top:38px;">Key Benefits</h2>
  <div class="slide-body" style="top:57px;">
    <p><strong>Marketing Opportunity</strong> Lorem Ipsum is simply dummy text of the printing and typesetting industry. Lorem Ipsum has been the industry's standard dummy text ever since the 1500s, when an unknown printer took a galley of type and scrambled it to make a type specimen book. It has survived not only five centuries, but also the leap into electronic typesetting.</p>
    <p><strong>Digital Guest Services</strong> Lorem Ipsum is simply dummy text of the printing and typesetting industry. Lorem Ipsum has been the industry's standard dummy text ever since the 1500s, when an unknown printer took a galley of type and scrambled it to make a type specimen book. It has survived not only five centuries, but also the leap into electronic typesetting, remaining essentially unchanged.</p>
  </div>
  <span class="url url--footer">www.snugstaypad.example</span>
</section>

<!-- Thank you -->
<section class="slide slide--cover" style="left:291px; top:948px;">
  <svg class="swoosh"><use href="#coverSwoosh"/></svg>
  <div class="brand brand--large"><span class="dot"></span>Snug Stay</div>
  <span class="brand-tag" style="left:208px; top:46px;">HOTEL TECHNOLOGY SOLUTIONS</span>
  <h1 class="cover-title" style="top:137px;">Thank you very much</h1>
  <p class="cover-sub">for your valuable time</p>
  <div class="contact">
    Contact us: <b>Alex Marlow</b>
    <div class="mail"><i></i>info@snugstaypad.example</div>
  </div>
</section>

</body>
</html>
```